Modern, corporate management consultancy firm needs a new website

We need a website for an Australian based management consultancy firm.

The company name is Corbel Strategy Partners.

We are looking for a parallax style wordpress site.

The site needs to provide the following functions:

1) subscribe function
2) links to social media (twitter, linkedin and mail)
3) a gated document section where people can download pdf's from the site after registering or providing name, company, position, email and contact number.

Attached is the company logo, would like to see designs that incorporate the dark blue and silver in the logo and separated into the following sections (Home, About, Services (with 4 options), Our Team, Links, Contacts.

Need the site to be easy to navigate and updated.

Potentially a News Section that can be updated regularly.

Target Market(s)

Target market is SME, business owners and directors

Industry/Entity Type

Management Consulting

Coding

Coded - Design and coding required

Number of Pages Required

1 page

Font styles to use
Sans Serif

Colors
0255a3
cbcbcb
757575
000000

Requirements
Must have
• Must be easy to read and use
Nice to have
• Features are listed on initial brief

```html
<!DOCTYPE html>
<html lang="en">
<head>
<meta charset="utf-8">
<title>Corbel Strategy Partners</title>
<link rel="stylesheet" href="https://fonts.googleapis.com/css2?family=Open+Sans:wght@400;600;700&display=swap">
<style>
  :root{
    --ink:#1d1d1d;
    --footer:#202020;
    --silver:#cbcbcb;
    --grey:#757575;
    --line:#d4d4d4;
    --paper:#ffffff;
    --blue:#0255a3;
    --footer-text:#bdbdbd;
  }
  *{box-sizing:border-box;margin:0;padding:0}
  html,body{width:857px;height:1200px;overflow:hidden;background:var(--paper)}
  body{font-family:"Open Sans",Arial,sans-serif;color:var(--ink);position:relative}

  .site-header{position:absolute;top:0;left:0;width:857px;height:385px;overflow:hidden}
  .hero-photo{position:absolute;inset:0;background:radial-gradient(ellipse at 70% 60%,#5a5f66 0%,#34383d 45%,#1c1e21 100%)}
  .topbar{position:absolute;top:0;left:0;right:0;height:30px;background:rgba(20,20,20,.85);display:flex;align-items:center;justify-content:space-between;padding:0 64px 0 80px}
  .brand{display:flex;align-items:center;gap:7px;color:#fff;font-size:9px;font-weight:600;letter-spacing:.3px;white-space:nowrap}
  .brand-dot{width:14px;height:14px;border-radius:50%;background:#fff;flex:none}
  .main-nav{display:flex;gap:16px}
  .main-nav a{color:#cfcfcf;font-size:7px;text-decoration:none;text-transform:uppercase;letter-spacing:.4px}
  .hero-title{position:absolute;top:188px;left:0;right:0;text-align:center;color:#fff;font-size:25px;font-weight:600;letter-spacing:1.5px}
  .btn-hero{position:absolute;top:307px;left:375px;width:107px;height:22px;border:1px solid #fff;border-radius:11px;color:#fff;font-size:8px;display:flex;align-items:center;justify-content:center;letter-spacing:.8px}

  .news{position:absolute;top:385px;left:0;width:857px}
  .news-heading{display:flex;align-items:center;justify-content:center;gap:22px;margin-top:34px;height:30px}
  .news-heading .rule{width:150px;height:1px;background:var(--ink)}
  .news-heading h2{font-size:25px;font-weight:600;letter-spacing:5px}
  .article{position:absolute;left:163px;width:508px;height:192px;display:flex}
  .article-photo{width:262px;height:100%;flex:none}
  .article-body{width:246px;padding:28px 0 0 22px}
  .article.reverse{flex-direction:row-reverse}
  .article.reverse .article-body{padding:28px 22px 0 4px}
  .article-body h3{font-size:12px;font-weight:600;letter-spacing:.5px;margin-bottom:6px}
  .article-body .underline{width:160px;height:1px;background:var(--line);margin-bottom:10px}
  .article-body p{font-size:6.3px;line-height:1.5;color:var(--grey);margin-bottom:14px}
  .btn-more{display:inline-block;padding:4px 14px;border:1px solid var(--silver);border-radius:10px;font-size:6px;color:var(--grey);text-transform:uppercase;letter-spacing:.5px}

  .photo-handshake{background:linear-gradient(135deg,#c9c9c9,#6e6e6e 60%,#3b3b3b)}
  .photo-team{background:linear-gradient(135deg,#e6e8ea,#a9b0b8 55%,#5a6470)}
  .photo-meeting{background:linear-gradient(135deg,#dcdcdc,#8f9398 55%,#3e4247)}

  .site-footer{position:absolute;top:1112px;left:0;width:857px;height:88px;background:var(--footer);color:var(--footer-text);display:flex;padding:22px 0 0 163px;font-size:6.5px}
  .footer-brand{width:108px;display:flex;align-items:center;gap:6px;color:#fff;font-size:7.5px;font-weight:600;line-height:1.25;align-self:flex-start}
  .contact{width:122px;display:flex;flex-direction:column;gap:9px}
  .contact li{list-style:none;display:flex;gap:6px;align-items:flex-start;line-height:1.4}
  .contact svg{flex:none;margin-top:1px}
  .footer-col{width:80px}
  .footer-col h4{color:#fff;font-size:7px;font-weight:600;margin-bottom:5px;height:10px}
  .footer-col li{list-style:none;line-height:1.7}
  .social{margin-left:auto;margin-right:160px;display:flex;gap:6px}
  .social span{width:14px;height:14px;border-radius:50%;background:#6a6a6a}
</style>
</head>
<body>
  <header class="site-header">
    <div class="hero-photo" role="img" aria-label="Hand of a businessman touching a glowing network of connected circles"></div>
    <div class="topbar">
      <div class="brand"><span class="brand-dot"></span>Corbel Strategy Partners</div>
      <nav class="main-nav">
        <a>Home</a><a>About</a><a>Services</a><a>Our Team</a><a>Links</a><a>Contacts</a>
      </nav>
    </div>
    <h1 class="hero-title">WE IMPROVE YOUR BUSINESS</h1>
    <div class="btn-hero">START NOW</div>
  </header>

  <section class="news">
    <div class="news-heading"><span class="rule"></span><h2>NEWS</h2><span class="rule"></span></div>
  </section>

  <article class="article" style="top:486px">
    <div class="article-photo photo-handshake" role="img" aria-label="Two businesspeople shaking hands"></div>
    <div class="article-body">
      <h3>ARTICLE TITLE</h3><div class="underline"></div>
      <p>Our advisers work beside owners and directors to sharpen strategy, tighten operations and build teams that grow. Read how a recent engagement helped one client lift margins and plan the next stage with confidence.</p>
      <span class="btn-more">Learn more</span>
    </div>
  </article>

  <article class="article reverse" style="top:680px">
    <div class="article-photo photo-team" role="img" aria-label="Businesswoman holding folders in front of her team"></div>
    <div class="article-body">
      <h3>ARTICLE TITLE</h3><div class="underline"></div>
      <p>Our advisers work beside owners and directors to sharpen strategy, tighten operations and build teams that grow. Read how a recent engagement helped one client lift margins and plan the next stage with confidence.</p>
      <span class="btn-more">Learn more</span>
    </div>
  </article>

  <article class="article" style="top:876px">
    <div class="article-photo photo-meeting" role="img" aria-label="Team meeting around a table with documents and laptops"></div>
    <div class="article-body">
      <h3>ARTICLE TITLE</h3><div class="underline"></div>
      <p>Our advisers work beside owners and directors to sharpen strategy, tighten operations and build teams that grow. Read how a recent engagement helped one client lift margins and plan the next stage with confidence.</p>
      <span class="btn-more">Learn more</span>
    </div>
  </article>

  <footer class="site-footer">
    <div class="footer-brand"><span class="brand-dot"></span><span>Corbel Strategy<br>Partners</span></div>
    <ul class="contact">
      <li><svg width="8" height="8" viewBox="0 0 10 10"><path d="M2 1l2 2-1 1.5a6 6 0 0 0 2.5 2.5L7 6l2 2-1.5 1.5C4 9 1 6 .5 2.5z" fill="#bdbdbd"/></svg>+61 2 5550 4821</li>
      <li><svg width="8" height="8" viewBox="0 0 10 10"><rect x=".5" y="2" width="9" height="6" fill="none" stroke="#bdbdbd"/><path d="M.5 2l4.5 3.5L9.5 2" fill="none" stroke="#bdbdbd"/></svg>hello@corbelstrategy.example</li>
      <li><svg width="8" height="8" viewBox="0 0 10 10"><path d="M5 .5a3.5 3.5 0 0 1 3.5 3.5C8.5 6.5 5 9.5 5 9.5S1.5 6.5 1.5 4A3.5 3.5 0 0 1 5 .5z" fill="#bdbdbd"/></svg>Level 4, 18 Wattlegum Lane,<br>Brindabella Heights</li>
    </ul>
    <div class="footer-col">
      <h4>About us</h4>
      <ul><li>Our story</li><li>Services</li><li>Our Team</li><li>News</li></ul>
    </div>
    <div class="footer-col">
      <h4></h4>
      <ul><li>Links</li><li>Contacts</li><li>Subscribe</li><li>Downloads</li></ul>
    </div>
    <div class="social"><span></span><span></span><span></span></div>
  </footer>
</body>
</html>
```